New business card with our logo

we finalized our logo with the help of pixel harbor - now we need a business card using that logo. we are a metal service center providing raw steel and metal products for fabricating, contractors, artists, etc. we have the wording for the back of the card figured out (attached, no deviations from text please), just need help putting it all together.
would like the look of steel somehow incorporated in the design ... would like the black part of the logo to be steel or silver color (the S & BRANLEY)
Other font styles liked:
- calibri, arial, similar to those, modern looking
Colors
Designer to choose colors to be used in the design.
Requirements
Must have
- Back of card must haves are attached (no deviations from wording please).
- FRONT of card:
- logo
- address
- name
- office tel
- cell
- fax
- website
- address
Nice to have
- incorporate the look of steel or element of steel somehow
- names of the staff on front not in all caps, i.e. Rosvita not ROSVITA
- this industry is more industrial, not coffee or flower shop so design should be aligned with that
- design should be classic and tasteful

```html
<!DOCTYPE html>
<html lang="en">
<head>
<meta charset="utf-8">
<title>Branley Steel – Business Card</title>
<link href="https://fonts.googleapis.com/css2?family=Figtree:wght@400;600;700&display=swap" rel="stylesheet">
<style>
  :root {
    --bg: #2c2c2c;
    --card-white: #ffffff;
    --steel-blue: #0a6fb9;
    --ink: #2a2a2a;
    --muted: #555a60;
    --on-blue: #ffffff;
  }
  * { box-sizing: border-box; margin: 0; padding: 0; }
  html, body { width: 1200px; height: 960px; overflow: hidden; }
  body {
    background: var(--bg);
    font-family: "Figtree", Arial, sans-serif;
    position: relative;
  }
  .card {
    position: absolute;
    left: 272px;
    width: 656px;
    height: 374px;
    border-radius: 18px;
    overflow: hidden;
  }
  .card-front { top: 80px; background: var(--card-white); }
  .card-back { top: 506px; background: var(--steel-blue); color: var(--on-blue); }

  .brand { position: absolute; display: flex; align-items: center; }
  .brand-ring { border-radius: 50%; flex: none; }
  .brand-name { font-weight: 700; letter-spacing: 0.2px; white-space: nowrap; }

  .card-front .brand { left: 40px; top: 39px; }
  .card-front .brand-ring { width: 68px; height: 68px; border: 5px solid var(--steel-blue); }
  .card-front .brand-name { margin-left: 14px; font-size: 37px; color: var(--steel-blue); }

  .person { position: absolute; right: 50px; top: 166px; text-align: right; }
  .person-name { font-size: 24px; font-weight: 700; color: var(--steel-blue); line-height: 27px; }
  .person-title { font-size: 17.5px; color: var(--muted); line-height: 24px; }

  .contact-list { position: absolute; left: 42px; top: 230px; list-style: none; }
  .contact-list li {
    display: flex; align-items: center; height: 22.2px;
    font-size: 15px; color: var(--muted);
  }
  .contact-list svg { width: 12px; height: 12px; margin-right: 8px; fill: var(--steel-blue); flex: none; }

  .address { position: absolute; right: 50px; top: 271px; text-align: right; font-size: 15.5px; line-height: 22.5px; color: var(--muted); }
  .address-company { font-weight: 700; color: var(--steel-blue); }

  .card-back .brand { left: 128px; top: 63px; }
  .card-back .brand-ring { width: 94px; height: 94px; border: 6px solid var(--on-blue); }
  .card-back .brand-name { margin-left: 136px; margin-left: 136px; font-size: 48px; position: absolute; left: -28px; white-space: nowrap; }
  .card-back .brand-name { left: 102px; margin-left: 0; }

  .services { position: absolute; left: 230px; top: 173px; font-size: 15.5px; line-height: 22px; }
  .services p { white-space: nowrap; }
  .services-title { font-weight: 700; }
  .services .divider { width: 64px; height: 1.5px; background: var(--on-blue); margin: 10px 0 10px 26px; }
</style>
</head>
<body>

<section class="card card-front">
  <div class="brand">
    <span class="brand-ring"></span>
    <span class="brand-name">BRANLEY STEEL</span>
  </div>

  <div class="person">
    <p class="person-name">DANE WHITCOMBE</p>
    <p class="person-title">President &amp; CEO</p>
  </div>

  <ul class="contact-list">
    <li><svg viewBox="0 0 12 12"><path d="M3 1l2 2.5-1.2 1.3a7 7 0 0 0 3.4 3.4L8.5 7 11 9l-1 2C5 11 1 7 1 2z"/></svg>123.123.1234</li>
    <li><svg viewBox="0 0 12 12"><path d="M3 0h6v12H3zM4.2 1.2v8.6h3.6V1.2z"/></svg>123.123.1234</li>
    <li><svg viewBox="0 0 12 12"><path d="M3 0h6v3H3zM1 4h10v5H9v3H3V9H1zM4 8v3h4V8z"/></svg>123.123.1234</li>
    <li><svg viewBox="0 0 12 12"><path d="M0 2h12v8H0zM1 3l5 4 5-4v-.3H1z"/></svg>info@BranleySteel.com</li>
    <li><svg viewBox="0 0 12 12"><path d="M6 0a6 6 0 1 0 0 12A6 6 0 0 0 6 0zm0 1.2c.7.8 1.2 2.3 1.3 4.2H4.7C4.8 3.5 5.3 2 6 1.2zM1.2 6.6h2.3c.1 1.7.5 3.1 1.1 4A4.8 4.8 0 0 1 1.2 6.6zm0-1.2A4.8 4.8 0 0 1 4.6 1.4c-.6.9-1 2.3-1.1 4zm4.8 5.4c-.7-.8-1.2-2.3-1.3-4.2h2.6C7.2 8.5 6.7 10 6 10.8zm1.4-.2c.6-.9 1-2.3 1.1-4h2.3a4.8 4.8 0 0 1-3.4 4zm1.1-5.2c-.1-1.7-.5-3.1-1.1-4a4.8 4.8 0 0 1 3.4 4z"/></svg>www.BranleySteel.com</li>
  </ul>

  <div class="address">
    <p class="address-company">BranleySteel</p>
    <p>4810 Forge Park Dr, Suite 210</p>
    <p>Millbrook, NC 27390</p>
  </div>
</section>

<section class="card card-back">
  <div class="brand">
    <span class="brand-ring"></span>
    <span class="brand-name">BRANLEY STEEL</span>
  </div>

  <div class="services">
    <p class="services-title">Metal Service Center</p>
    <p>Cut &nbsp;-&nbsp; Shear &nbsp;-&nbsp; Punch &nbsp;-&nbsp; Light Fab</p>
    <div class="divider"></div>
    <p>Structural Steel &nbsp;-&nbsp; Stainless &amp; Aluminum</p>
    <p>Building Components &nbsp;-&nbsp; Rebar &nbsp;-&nbsp; Decking and More!</p>
    <div class="divider"></div>
    <p>Cut to size, Pick-up or Delivered</p>
  </div>
</section>

</body>
</html>
```